RW Stewardship real estate management company needs presentation folder to hand clients

looking for a folder with pockets that represent my real estate management company when i hand to client reports or promotional material. I only do resedential real estate. I want classy and professional - pictures or additioal graphixs are fine

when a client open i will usally insert text and reports about my business
also on the inside flap is usally place for my business card i will upload a picture so the theme can be constant

Target Market(s)

my existing real estate cleints
and i will use when i am soliciting new business

Industry/Entity Type

Real Estate

Font styles to use
Serif

Requirements
Must have
• must have logo
• must give appearance of professionalism and maturity
• have basic company info tel# ,address
• id like viewer to know I manage real estate - focus on residential small to large apartment buildings
• not strip malls, not giganic complexes - im a mid size company
• logo is black but i welcome color as u see fit
Nice to have
• maybe pictures
• my slogan - " we will manage your building like its our own "
• focus on professioanl, safe, trust worthy
• type style should be clear and readable - but im open to sugestions

```html
<!DOCTYPE html>
<html lang="en">
<head>
<meta charset="utf-8">
<title>RW Stewardship — Presentation Folder</title>
<link href="https://fonts.googleapis.com/css2?family=Roboto:wght@400;700;900&family=Playfair+Display:ital,wght@0,700;1,700&display=swap" rel="stylesheet">
<style>
  :root {
    --page: #ffffff;
    --ink: #000000;
    --cover: #000000;
    --panel: #f1f1f1;
    --panel-edge: #e4e4e4;
    --sheet: #ffffff;
    --pocket: #1c1c1c;
    --text-body: #222222;
    --faint: #c9c9c9;
    --white: #ffffff;
  }
  * { box-sizing: border-box; margin: 0; padding: 0; }
  html, body { width: 1200px; height: 1000px; overflow: hidden; background: var(--page); }
  body { position: relative; font-family: "Roboto", Arial, sans-serif; color: var(--ink); }

  /* Front cover */
  .front-cover { position: absolute; left: 127px; top: 433px; width: 277px; height: 388px; background: var(--cover); }
  .cover-band { position: absolute; left: 0; top: 120px; width: 277px; height: 72px; display: flex; }
  .cover-band .photo { flex: 1; }
  .photo { display: block; }
  .gray-1 { background: linear-gradient(180deg, #9a9a9a, #6d6d6d); }
  .gray-2 { background: linear-gradient(180deg, #b5b5b5, #7c7c7c); }
  .gray-3 { background: linear-gradient(180deg, #d4d4d4, #a0a0a0); }
  .gray-4 { background: linear-gradient(180deg, #c4c4c4, #8a8a8a); }
  .cover-brand { position: absolute; right: 24px; bottom: 26px; display: flex; align-items: center; gap: 5px; color: var(--white); font-weight: 700; font-size: 11px; }
  .brand-mark { width: 9px; height: 9px; background: currentColor; }

  /* Inside spread */
  .inside-left { position: absolute; left: 508px; top: 437px; width: 272px; height: 385px; background: linear-gradient(180deg, #fafafa, var(--panel)); border-right: 1px solid var(--panel-edge); }
  .photo-grid .photo { position: absolute; }
  .ph-house { left: 21px; top: 43px; width: 74px; height: 72px; background: linear-gradient(180deg, #6fa6e0, #c9b79a); }
  .ph-couple { left: 103px; top: 43px; width: 74px; height: 72px; background: linear-gradient(180deg, #d7dde3, #7fc3d6); }
  .ph-towers { left: 21px; top: 124px; width: 156px; height: 73px; background: linear-gradient(135deg, #8fc2ee, #2f6fb0 60%, #1f4f85); }
  .ph-key { left: 185px; top: 43px; width: 74px; height: 235px; background: linear-gradient(180deg, #e9e9ea, #cfcfd1); }
  .ph-keys { left: 21px; top: 205px; width: 74px; height: 72px; background: linear-gradient(180deg, #f1efe9, #cbb98a); }
  .ph-meeting { left: 103px; top: 205px; width: 74px; height: 72px; background: linear-gradient(180deg, #e6e1d8, #8a7f74); }

  .inside-brand { position: absolute; left: 25px; top: 330px; display: flex; align-items: center; gap: 5px; font-weight: 700; font-size: 10px; color: var(--ink); }
  .contact-card { position: absolute; right: 20px; top: 318px; text-align: right; line-height: 1.15; }
  .contact-name { font-weight: 700; font-size: 11px; }
  .contact-title { font-size: 5.5px; letter-spacing: .2px; }
  .contact-lines { margin-top: 8px; font-size: 5.5px; }
  .contact-address { margin-top: 3px; font-size: 3.5px; }

  .inside-right { position: absolute; left: 784px; top: 437px; width: 273px; height: 385px; background: var(--panel); }
  .insert-sheet { position: absolute; left: 14px; top: 16px; width: 222px; height: 300px; background: var(--sheet); box-shadow: 0 0 3px rgba(0,0,0,.12); padding: 22px 14px 0 28px; }
  .sheet-brand { margin-left: 2px; font-weight: 700; font-size: 7px; color: var(--faint); display: flex; align-items: center; gap: 3px; }
  .sheet-brand .brand-mark { width: 6px; height: 6px; }
  .sheet-text { margin-top: 14px; font-size: 4.6px; line-height: 1.45; color: var(--text-body); }
  .sheet-text p + p { margin-top: 7px; }

  .pocket { position: absolute; left: 11px; top: 256px; width: 262px; height: 129px; }
  .slogan { position: absolute; right: 14px; top: 61px; text-align: right; color: var(--white); line-height: 1; }
  .slogan-lead { font-family: "Playfair Display", Georgia, serif; font-style: italic; font-weight: 700; font-size: 12px; }
  .slogan-key { font-family: "Roboto", Arial, sans-serif; font-weight: 900; font-size: 20px; margin-top: 3px; }
  .slogan-tail { font-family: "Playfair Display", Georgia, serif; font-weight: 700; font-size: 7.5px; margin-top: 2px; }
</style>
</head>
<body>

  <section class="front-cover">
    <div class="cover-band">
      <div class="photo gray-1" role="img" aria-label="Grayscale photo of a suburban home"></div>
      <div class="photo gray-2" role="img" aria-label="Grayscale photo of a smiling couple"></div>
      <div class="photo gray-3" role="img" aria-label="Grayscale photo of house keys"></div>
      <div class="photo gray-4" role="img" aria-label="Grayscale photo of a property viewing"></div>
    </div>
    <div class="cover-brand"><span class="brand-mark"></span>RW Stewardship</div>
  </section>

  <section class="inside-left">
    <div class="photo-grid">
      <div class="photo ph-house" role="img" aria-label="Photo of a two-storey residential house"></div>
      <div class="photo ph-couple" role="img" aria-label="Photo of a couple holding new keys"></div>
      <div class="photo ph-towers" role="img" aria-label="Photo of glass apartment towers against the sky"></div>
      <div class="photo ph-key" role="img" aria-label="Photo of a hand holding a key with a house keychain"></div>
      <div class="photo ph-keys" role="img" aria-label="Photo of keys on paperwork"></div>
      <div class="photo ph-meeting" role="img" aria-label="Photo of a manager showing an apartment"></div>
    </div>
    <div class="inside-brand"><span class="brand-mark"></span>RW Stewardship</div>
    <div class="contact-card">
      <div class="contact-name">Daniel Marlow</div>
      <div class="contact-title">MASTER BUILDING MANAGER</div>
      <div class="contact-lines">
        <div>office tel: 914-555-0142</div>
        <div>email dmarlow@rwstewardship.com</div>
        <div>cell 917-555-0187</div>
      </div>
      <div class="contact-address">27 HARBOR LANE SUITE 3B RIDGEFIELD NY 10000</div>
    </div>
  </section>

  <section class="inside-right">
    <article class="insert-sheet">
      <div class="sheet-brand"><span class="brand-mark"></span>RW Stewardship</div>
      <div class="sheet-text">
        <p>Lorem Ipsum is simply dummy text of the printing and typesetting industry. Lorem Ipsum has been the industry's standard dummy text ever since the 1500s, when an unknown printer took a galley of type and scrambled it to make a type specimen book. It has survived not only five centuries, but also the leap into electronic typesetting, remaining essentially unchanged. It was popularised in the 1960s with the release of Letraset sheets containing Lorem Ipsum passages, and more recently with desktop publishing software including versions of Lorem Ipsum.</p>
        <p>It is a long established fact that a reader will be distracted by the readable content of a page when looking at its layout. The point of using Lorem Ipsum is that it has a more-or-less normal distribution of letters, as opposed to using 'Content here, content here', making it look like readable English. Many desktop publishing packages and web page editors now use Lorem Ipsum as their default model text, and a search for 'lorem ipsum' will uncover many web sites still in their infancy.</p>
        <p>Contrary to popular belief, Lorem Ipsum is not simply random text. It has roots in a piece of classical Latin literature from 45 BC, making it over 2000 years old. A Latin professor looked up one of the more obscure Latin words, consectetur, from a Lorem Ipsum passage, and going through the cites of the word in classical literature, discovered the undoubtable source. The generated Lorem Ipsum is therefore always free from repetition, injected humour, or non-characteristic words etc.</p>
      </div>
    </article>
    <div class="pocket">
      <svg width="262" height="129" viewBox="0 0 262 129" aria-hidden="true">
        <path d="M0 14 L14 0 L262 0 L262 129 L0 129 Z" fill="var(--pocket)"/>
      </svg>
      <div class="slogan">
        <div class="slogan-lead">We will manage your</div>
        <div class="slogan-key">BUILDING</div>
        <div class="slogan-tail">LIKE ITS OUR OWN!</div>
      </div>
    </div>
  </section>

</body>
</html>
```